Marlowick APP redesign and color change

I am looking for a new design for my app. Please see the attached current design.

Currently, I have a functioning app but the colors and design are awful!
The logo is great but the rest of the app needs a refresh.
(Logo hi res not yet available but will upload soon.)
New colors or anything that is cutting edge.

Basically: It is a secure social media app within a school system where the teachers, students and parents can text, exchange photos, plan curriculum, etc.

I NEED ONLY landing page with a new look!
Looking for one distinct design for the landing page with new look.
The developer will apply this one design towards the rest of the pages/app screens.

Because part of the social media I need the feel and look of what is now the trend. Something that will attract and keep the client(s) interested. I am really leaving all the creative work to the designer and open to any suggestions.
Updates

Target Market(s)

Schools, community, teachers, students, colleges, sport teams

Industry/Entity Type

Non Profit

Font styles to use
Serif
Sans Serif

Colors

Designer to choose colors to be used in the design.

Requirements
Must have
• Sharp, trendy, millennial feel
Nice to have
• Up to designer
Should not have
• Up to designer

```html
<!DOCTYPE html>
<html lang="en">
<head>
<meta charset="utf-8">
<title>Marlowick — Sign in</title>
<link rel="stylesheet" href="https://fonts.googleapis.com/css2?family=Saira:wght@600;700&family=Open+Sans:wght@400;600&display=swap">
<style>
  :root {
    --canvas: #ecd3b4;
    --olive: #6d733f;
    --olive-deep: #5a6231;
    --olive-shade: #4d5428;
    --ink-olive: #4b5322;
    --white: #ffffff;
    --line: rgba(255, 255, 255, 0.75);
  }
  * { box-sizing: border-box; margin: 0; padding: 0; }
  html, body {
    width: 1200px;
    height: 939px;
    overflow: hidden;
    background: var(--canvas);
  }
  .app-screen {
    position: absolute;
    left: 362px;
    top: 40px;
    width: 475px;
    height: 860px;
    border-radius: 30px;
    overflow: hidden;
    background: var(--olive);
    box-shadow: 0 14px 34px rgba(90, 60, 30, 0.28);
  }
  .backdrop-photo {
    position: absolute;
    inset: 0;
    background:
      radial-gradient(ellipse at 30% 55%, rgba(140, 135, 85, 0.55), transparent 60%),
      radial-gradient(ellipse at 80% 25%, rgba(120, 125, 70, 0.5), transparent 55%),
      linear-gradient(180deg, #737a45 0%, #6a7040 55%, #656b3c 100%);
  }
  .brand {
    position: absolute;
    top: 190px;
    left: 0;
    width: 100%;
    display: flex;
    align-items: center;
    justify-content: center;
    gap: 12px;
  }
  .brand-dot {
    width: 16px;
    height: 16px;
    border-radius: 50%;
    background: var(--white);
  }
  .brand-name {
    font-family: "Saira", sans-serif;
    font-weight: 700;
    font-size: 34px;
    letter-spacing: 1px;
    color: var(--white);
    text-transform: uppercase;
  }
  .login-fields {
    position: absolute;
    left: 49px;
    top: 340px;
    width: 377px;
    height: 172px;
    border: 1.5px solid var(--line);
    border-radius: 9px;
  }
  .field {
    position: absolute;
    left: 31px;
    font-family: "Open Sans", sans-serif;
    font-size: 16px;
    color: var(--white);
  }
  .field-email { top: 37px; }
  .field-password { top: 113px; }
  .field-divider {
    position: absolute;
    left: 24px;
    right: 44px;
    top: 84px;
    height: 1px;
    background: var(--line);
  }
  .forgot-link {
    position: absolute;
    top: 552px;
    left: 0;
    width: 100%;
    text-align: center;
    font-family: "Open Sans", sans-serif;
    font-size: 16px;
    color: var(--white);
  }
  .btn {
    position: absolute;
    left: 49px;
    width: 377px;
    height: 58px;
    border-radius: 9px;
    display: flex;
    align-items: center;
    justify-content: center;
    font-family: "Saira", sans-serif;
    font-weight: 600;
    font-size: 23px;
    letter-spacing: 0.5px;
    text-transform: uppercase;
  }
  .btn-login {
    top: 612px;
    background: var(--white);
    color: var(--ink-olive);
    box-shadow: 0 4px 8px rgba(40, 45, 15, 0.3);
  }
  .btn-signup {
    top: 752px;
    background: var(--olive-deep);
    color: var(--white);
    box-shadow: 0 4px 8px rgba(40, 45, 15, 0.35);
  }
</style>
</head>
<body>
  <main class="app-screen">
    <div class="backdrop-photo" role="img" aria-label="Background photo of a young student in a hat using a phone, under an olive tint"></div>

    <div class="brand">
      <span class="brand-dot"></span>
      <span class="brand-name">Marlowick</span>
    </div>

    <div class="login-fields">
      <span class="field field-email">Email or Username</span>
      <span class="field-divider"></span>
      <span class="field field-password">Password</span>
    </div>

    <p class="forgot-link">Forget password ?</p>

    <div class="btn btn-login">Log in</div>
    <div class="btn btn-signup">Sign up</div>
  </main>
</body>
</html>
```